New Business Card Design Project

Use the flyer uploaded and website www.brightoakbuilders.com for inspiration.
List Our Services on Backside of business cards
Martin Hollis
Harborline Renovations Inc.
Licensed General Contractors
858-471-9063

Contact Information for Business Card

Use the flyer uploaded and website www.brightoakbuilders.com for inspiration. List Our Services on Backside of business cards Martin Hollis Harborline Renovations Inc. Licensed General Contractors 858-471-9063

```html
<!DOCTYPE html>
<html lang="en">
<head>
<meta charset="UTF-8">
<title>Harborline Renovations – Business Card</title>
<link rel="stylesheet" href="https://fonts.googleapis.com/css2?family=Lato:wght@400;700;900&display=swap">
<style>
  :root {
    --stage: #e4e4e2;
    --card-dark: #0d0d0d;
    --card-light: #ffffff;
    --ink: #111111;
    --ink-soft: #444444;
    --silver: #e6e6e6;
    --brand-blue: #2f7fd0;
    --brand-red: #e0262b;
    --rule-blue: #4a8fd8;
  }
  * { box-sizing: border-box; margin: 0; padding: 0; }
  html, body { width: 1200px; height: 900px; overflow: hidden; }
  body {
    background: var(--stage);
    font-family: "Lato", sans-serif;
    display: flex;
    flex-direction: column;
    align-items: center;
    justify-content: center;
    gap: 44px;
  }
  .card {
    width: 630px;
    height: 360px;
    border-radius: 22px;
    position: relative;
    overflow: hidden;
    box-shadow: 0 10px 28px rgba(0,0,0,.18);
  }

  /* Back side */
  .card--back {
    background: var(--card-dark);
    color: var(--silver);
    display: flex;
    flex-direction: column;
    align-items: center;
    justify-content: center;
    gap: 44px;
  }
  .back-brand {
    font-size: 38px;
    font-weight: 400;
    letter-spacing: 4px;
    text-transform: uppercase;
    color: var(--silver);
  }
  .services {
    text-align: center;
    font-size: 15px;
    letter-spacing: 1.4px;
    line-height: 1.7;
    text-transform: uppercase;
    color: #ffffff;
  }

  /* Front side */
  .card--front { background: var(--card-light); }
  .person {
    position: absolute;
    left: 44px;
    top: 70px;
    width: 290px;
  }
  .person-name {
    font-weight: 900;
    font-size: 34px;
    line-height: 1.1;
    color: var(--brand-blue);
    letter-spacing: .5px;
    text-transform: uppercase;
    white-space: nowrap;
  }
  .person-title {
    font-size: 19px;
    color: var(--brand-red);
    margin-top: 4px;
    letter-spacing: .3px;
    white-space: nowrap;
  }
  .front-brand {
    position: absolute;
    right: 44px;
    top: 78px;
    display: flex;
    align-items: center;
    gap: 12px;
    color: var(--ink);
  }
  .front-brand .mark {
    width: 12px;
    height: 12px;
    background: var(--ink);
    flex: none;
  }
  .front-brand .brand-name {
    font-size: 24px;
    font-weight: 400;
    letter-spacing: 2.5px;
    line-height: 1.2;
    text-transform: uppercase;
    text-align: left;
  }
  .divider {
    position: absolute;
    left: 40px;
    right: 40px;
    top: 168px;
    height: 1px;
    background: var(--rule-blue);
  }
  .contacts {
    position: absolute;
    left: 44px;
    top: 186px;
    list-style: none;
    display: flex;
    flex-direction: column;
    gap: 8px;
  }
  .contact {
    display: flex;
    align-items: center;
    gap: 10px;
    font-size: 17px;
    color: var(--ink-soft);
    white-space: nowrap;
  }
  .contact--phone { font-weight: 700; color: var(--ink); font-size: 19px; }
  .contact svg { width: 16px; height: 16px; flex: none; }
  .company {
    position: absolute;
    right: 44px;
    bottom: 34px;
    text-align: right;
  }
  .company-name {
    font-weight: 700;
    font-size: 19px;
    color: var(--brand-blue);
    margin-bottom: 4px;
  }
  .company-address {
    font-size: 17px;
    color: var(--ink-soft);
    line-height: 1.35;
  }
</style>
</head>
<body>

  <section class="card card--back" aria-label="Business card back">
    <div class="back-brand">Harborline Renovations</div>
    <p class="services">
      Painting | Flooring | Kitchens | Bathrooms<br>
      Energy Efficienct Upgrades | Custom Renovations
    </p>
  </section>

  <section class="card card--front" aria-label="Business card front">
    <div class="person">
      <h1 class="person-name">Martin Hollis</h1>
      <p class="person-title">Licensed General Contractors</p>
    </div>

    <div class="front-brand">
      <span class="mark"></span>
      <span class="brand-name">Harborline<br>Renovations</span>
    </div>

    <div class="divider"></div>

    <ul class="contacts">
      <li class="contact contact--phone">
        <svg viewBox="0 0 24 24" fill="var(--brand-blue)"><path d="M6.6 10.8a15.1 15.1 0 006.6 6.6l2.2-2.2c.3-.3.7-.4 1-.2 1.1.4 2.3.6 3.6.6.6 0 1 .4 1 1V20c0 .6-.4 1-1 1A17 17 0 013 4c0-.6.4-1 1-1h3.5c.6 0 1 .4 1 1 0 1.3.2 2.5.6 3.6.1.3 0 .7-.2 1z"/></svg>
        858-471-9063 Call/Text
      </li>
      <li class="contact">
        <svg viewBox="0 0 24 24" fill="var(--brand-blue)"><path d="M2 5h20v14H2z" opacity=".25"/><path d="M2 5h20v14H2zM4 7v.4l8 5.3 8-5.3V7zm0 2.8V17h16V9.8l-8 5.3z"/></svg>
        info@brightoakbuilders.com
      </li>
      <li class="contact">
        <svg viewBox="0 0 24 24" fill="none" stroke="var(--brand-blue)" stroke-width="2"><circle cx="12" cy="12" r="9"/><path d="M3 12h18M12 3c3 3 3 15 0 18M12 3c-3 3-3 15 0 18"/></svg>
        brightoakbuilders.com
      </li>
    </ul>

    <div class="company">
      <p class="company-name">Harborline Renovations Inc.</p>
      <p class="company-address">Your Address, City<br>State, Zip 1235</p>
    </div>
  </section>

</body>
</html>
```